New Business card design to reflect rebrand

I would like a business card design with a good base colour for our new logo and also a placeholder for a profile pic of the card holder. the design needs to be editable to the point that we can easily change the picture of the person and use that design for printmoor etc. we are looking at a metalic finish business card so will need a good base colour to bring out the finish.

Target Market(s)

prospective customers

Industry/Entity Type

Business

Contact Information for Business Card

I would like one editable design that we can change the name of the card holder and profile picture. The design need to be in a format that be send to printmoor etc.

Our address is Fenwick Lodge, Mill Lane, Ashcombe Green, RG41 3TQ Tel no. 01632 960417

Requirements
Must have
• place holder for a profile pic for the card holder. in AI or preferably PSD format

```html
<!DOCTYPE html>
<html lang="en">
<head>
<meta charset="utf-8">
<title>Halden Workplace Services – Business Card</title>
<link href="https://fonts.googleapis.com/css2?family=Open+Sans:wght@400;600;700&display=swap" rel="stylesheet">
<style>
  :root {
    --navy: #3f5470;
    --orange: #ef6a22;
    --white: #ffffff;
    --stage: #2a2a2c;
    --avatar-bg: #86a6c4;
    --text-navy: #3b4d66;
  }
  * { box-sizing: border-box; margin: 0; padding: 0; }
  html, body {
    width: 1200px; height: 900px; overflow: hidden;
    background: var(--stage);
    font-family: "Open Sans", Arial, sans-serif;
  }
  .stage { position: relative; width: 1200px; height: 900px; }

  .card {
    position: absolute; top: 150px;
    width: 340px; height: 600px;
    overflow: hidden;
    box-shadow: 0 18px 40px rgba(0,0,0,.45);
  }

  /* Brand lockup */
  .brand {
    display: flex; align-items: center; justify-content: center; gap: 12px;
  }
  .brand-mark { width: 18px; height: 18px; background: var(--orange); flex: none; }
  .brand-name {
    font-weight: 700; font-size: 22px; line-height: 1.15;
    letter-spacing: .4px; color: var(--text-navy); text-align: left;
  }

  /* Front */
  .card--front { left: 190px; background: var(--white); }
  .front__brand { position: absolute; top: 44px; left: 0; width: 100%; }
  .avatar {
    position: absolute; top: 124px; left: 50%; transform: translateX(-50%);
    width: 164px; height: 164px; border-radius: 50%;
    border: 4px solid var(--orange);
    padding: 6px; background: var(--white);
  }
  .avatar__photo {
    width: 100%; height: 100%; border-radius: 50%;
    background: radial-gradient(circle at 50% 40%, #9bb7d1, var(--avatar-bg));
  }
  .holder { position: absolute; top: 298px; width: 100%; text-align: center; }
  .holder__name { font-weight: 700; font-size: 26px; line-height: 1.2; color: var(--text-navy); }
  .holder__title { font-weight: 600; font-size: 18px; line-height: 1.2; color: var(--orange); margin-top: 2px; }

  .front__contact {
    position: absolute; left: 0; bottom: 0;
    width: 100%; height: 218px; background: var(--navy);
    padding-top: 30px;
  }
  .front__contact::before {
    content: ""; position: absolute; top: -12px; left: 50%;
    transform: translateX(-50%);
    border-left: 12px solid transparent; border-right: 12px solid transparent;
    border-bottom: 12px solid var(--navy);
  }
  .contact-row { display: flex; align-items: center; height: 34px; margin-bottom: 10px; }
  .contact-row__tab {
    width: 58px; height: 30px; flex: none;
    background: var(--orange);
    border-radius: 0 15px 15px 0;
    display: flex; align-items: center; justify-content: center;
  }
  .contact-row__tab svg { width: 17px; height: 17px; }
  .contact-row__text {
    margin-left: 14px; color: var(--white);
    font-size: 18px; letter-spacing: .4px; white-space: nowrap;
  }
  .contact-row__text--address { font-size: 12px; line-height: 1.3; letter-spacing: .2px; white-space: normal; }

  /* Back */
  .card--back { left: 670px; background: var(--navy); }
  .back__bar {
    position: absolute; height: 14px; width: 215px;
    background: var(--orange); border-radius: 7px;
  }
  .back__bar--top { top: 18px; left: -7px; }
  .back__bar--bottom { bottom: 18px; right: -7px; }
  .back__brand {
    position: absolute; top: 50%; left: 0; width: 100%;
    transform: translateY(-50%);
  }
  .back__brand .brand-name { color: var(--white); font-size: 26px; }
  .back__brand .brand-mark { width: 22px; height: 22px; }
</style>
</head>
<body>
<main class="stage">

  <section class="card card--front" aria-label="Business card front">
    <div class="front__brand brand">
      <span class="brand-mark"></span>
      <span class="brand-name">Halden<br>Workplace Services</span>
    </div>

    <div class="avatar">
      <div class="avatar__photo" role="img" aria-label="Profile photo of the card holder"></div>
    </div>

    <div class="holder">
      <p class="holder__name">Your Name</p>
      <p class="holder__title">Title</p>
    </div>

    <div class="front__contact">
      <div class="contact-row">
        <span class="contact-row__tab">
          <svg viewBox="0 0 24 24" fill="none" stroke="#fff" stroke-width="2"><circle cx="12" cy="12" r="10"/><path d="M12 18s-4-4.5-4-7.5a4 4 0 0 1 8 0c0 3-4 7.5-4 7.5z"/><circle cx="12" cy="10.5" r="1.3" fill="#fff"/></svg>
        </span>
        <span class="contact-row__text contact-row__text--address">Fenwick Lodge,<br>Mill Lane, Ashcombe Green, RG41 3TQ</span>
      </div>
      <div class="contact-row">
        <span class="contact-row__tab">
          <svg viewBox="0 0 24 24" fill="none" stroke="#fff" stroke-width="2"><circle cx="12" cy="12" r="10"/><path d="M9 7.5l1.5 2.5-1 1.2a7 7 0 0 0 3.3 3.3l1.2-1 2.5 1.5-.8 1.8c-4 0-8.3-4.3-8.3-8.3z"/></svg>
        </span>
        <span class="contact-row__text">01632 960417</span>
      </div>
      <div class="contact-row">
        <span class="contact-row__tab">
          <svg viewBox="0 0 24 24" fill="none" stroke="#fff" stroke-width="2"><rect x="3" y="6" width="18" height="12" rx="1"/><path d="M3 7l9 6 9-6"/></svg>
        </span>
        <span class="contact-row__text">info@haldenws.co.uk</span>
      </div>
      <div class="contact-row">
        <span class="contact-row__tab">
          <svg viewBox="0 0 24 24" fill="none" stroke="#fff" stroke-width="1.8"><circle cx="12" cy="12" r="9"/><ellipse cx="12" cy="12" rx="4" ry="9"/><path d="M3 12h18M4.5 7.5h15M4.5 16.5h15"/></svg>
        </span>
        <span class="contact-row__text">www.haldenws.co.uk</span>
      </div>
    </div>
  </section>

  <section class="card card--back" aria-label="Business card back">
    <span class="back__bar back__bar--top"></span>
    <div class="back__brand brand">
      <span class="brand-mark"></span>
      <span class="brand-name">Halden<br>Workplace Services</span>
    </div>
    <span class="back__bar back__bar--bottom"></span>
  </section>

</main>
</body>
</html>
```